Want a package created for a new protein bar

We would like a new package created for a new protein bar project The name of the bar will be VOLMBite a real food protein bar, we would like a ‘window’ on the package of bar like Brave Meadow bar below in images.

VOLMBite
‘Super Food Bar’
14g of Whey Protein
The package film size is the following 12cm width x 15cm Length,
Flavor Peanut Chocolate Chip, additional information will be attached shortly like nutrition facts,

Target Market(s)

fitness market, bodybuilders, athletes, everyday people

Industry/Entity Type

Health Product

Logo Text

VOLMBite

Font styles to use
Serif
Sans Serif
Decorative

Requirements
Must have
• Package window

```html
<!DOCTYPE html>
<html lang="en">
<head>
<meta charset="utf-8">
<title>VOLMBite Protein Bar Wrapper</title>
<link rel="stylesheet" href="https://fonts.googleapis.com/css2?family=Montserrat:wght@300;400;700;800&family=Roboto:wght@500&display=swap">
<style>
  :root {
    --backdrop: #bccf8c;
    --green-bright: #2f8a2a;
    --green-mid: #1f6a25;
    --green-deep: #123c20;
    --green-ink: #0f3a1f;
    --white: #ffffff;
    --window-light: #e6a24c;
    --window-dark: #9a5a22;
  }
  html, body {
    margin: 0;
    width: 1200px;
    height: 800px;
    overflow: hidden;
    background: var(--backdrop);
  }
  .canvas {
    position: relative;
    width: 1200px;
    height: 800px;
    font-family: "Montserrat", sans-serif;
  }
  .wrapper-art {
    position: absolute;
    left: 0;
    top: 0;
  }
  .brand-name {
    position: absolute;
    left: 330px;
    top: 348px;
    margin: 0;
    font-weight: 400;
    font-size: 58px;
    letter-spacing: 10px;
    color: var(--green-ink);
    line-height: 1;
  }
  .product-type {
    position: absolute;
    left: 745px;
    top: 312px;
    margin: 0;
    font-family: "Roboto", sans-serif;
    font-weight: 500;
    font-size: 12px;
    line-height: 1.1;
    color: var(--white);
  }
  .weight-badge {
    position: absolute;
    left: 175px;
    top: 448px;
    width: 86px;
    height: 72px;
    border: 2px solid var(--white);
    border-radius: 6px;
    background: var(--green-deep);
    color: var(--white);
    font-family: "Roboto", sans-serif;
    font-weight: 500;
    font-size: 40px;
    display: flex;
    align-items: center;
    justify-content: center;
    box-sizing: border-box;
  }
  .claim {
    position: absolute;
    left: 282px;
    top: 448px;
    margin: 0;
    font-weight: 300;
    font-size: 17px;
    letter-spacing: 4px;
    color: var(--white);
  }
  .flavours {
    position: absolute;
    left: 282px;
    top: 474px;
    margin: 0;
    font-weight: 800;
    font-size: 26px;
    letter-spacing: 2px;
    color: var(--white);
  }
  .layer-badge {
    position: absolute;
    left: 925px;
    top: 252px;
    width: 96px;
    height: 74px;
    border: 2px solid var(--white);
    box-sizing: border-box;
    background: var(--white);
    display: flex;
    flex-direction: column;
  }
  .layer-badge-text {
    flex: 1;
    margin: 0;
    font-family: "Roboto", sans-serif;
    font-weight: 500;
    font-size: 15px;
    line-height: 1.05;
    text-align: center;
    color: var(--green-ink);
    padding-top: 6px;
  }
  .layer-badge-strip {
    height: 20px;
    background: var(--green-bright);
  }
</style>
</head>
<body>
<main class="canvas">
  <svg class="wrapper-art" width="1200" height="800" viewBox="0 0 1200 800">
    <defs>
      <linearGradient id="wrapperFill" x1="0" y1="0" x2="1" y2="0">
        <stop offset="0" stop-color="var(--green-bright)"/>
        <stop offset="0.5" stop-color="var(--green-mid)"/>
        <stop offset="1" stop-color="var(--green-deep)"/>
      </linearGradient>
      <linearGradient id="windowFill" x1="0" y1="0" x2="1" y2="1">
        <stop offset="0" stop-color="var(--window-light)"/>
        <stop offset="1" stop-color="var(--window-dark)"/>
      </linearGradient>
    </defs>
    <path class="wrapper-body" fill="url(#wrapperFill)"
      d="M100,240 H1100 L1085,260 L1100,280 L1085,300 L1100,320 L1085,340 L1100,360 L1085,380 L1100,400 L1085,420 L1100,440 L1085,460 L1100,480 L1085,500 L1100,520 L1085,540 L1100,560 H100 L115,540 L100,520 L115,500 L100,480 L115,460 L100,440 L115,420 L100,400 L115,380 L100,360 L115,340 L100,320 L115,300 L100,280 L115,260 Z"/>
    <rect class="crimp-shade" x="115" y="240" width="40" height="320" fill="#ffffff" opacity="0.12"/>
    <rect class="crimp-shade" x="1045" y="240" width="40" height="320" fill="#000000" opacity="0.18"/>
    <rect class="white-band" x="100" y="345" width="760" height="72" fill="var(--white)"/>
    <polygon class="bar-window" points="870,240 1045,240 1045,560 840,560" fill="url(#windowFill)"
      role="img" aria-label="Window showing the peanut and chocolate chip bar inside"/>
  </svg>

  <h1 class="brand-name">VOLMBite</h1>
  <p class="product-type">PROTEIN<br>BAR</p>

  <div class="weight-badge">20g</div>
  <p class="claim">100% NATURAL</p>
  <p class="flavours">PEANUT | CHOCOLATE | SUGAR</p>

  <div class="layer-badge">
    <p class="layer-badge-text">DOUBLE<br>LAYER</p>
    <div class="layer-badge-strip"></div>
  </div>
</main>
</body>
</html>
```